How our User's connect on our Platform with Health Providers Graphic

We'd like a clean simple graphic that shows how our Platform connects our Users with our Wellness related Facilities and other "Connected" People.

User is at the Center of our Graphic.

4 Wellness based Facility Types are connected to the User.
1. Mind
2. Body
3. Spirit
4. Heart

Then in between the 4 Wellness Facilities there are People who are connected to the 4 Facility Types and to the User as well.
1. Family
2. Friends
3. Acquaintances
4. Professionals

Our Company is called Brava

We use our Brava Stone Logo

Our 2 main Colors are
#1D44B8 - Blue
#D85097 - Pink

Secondary Colors are
#D0E1F7 - Light Blue
#1D44B8 - Blue
#D85097 - Pink
#F7E1F5 - Light Pink
#F2E6FF - Lavender
#F0F4FF - Light Blue

Could try using the screen shot of our App in the center..... then show how it's connected to the 4 Types of Providers and our Connections

Target Market(s)

Admins of Nursing Homes, Hospitals, Doctors offices and other Health Related Businesses.

Industry/Entity Type

Health And Wellness

Font styles to use
Other font styles liked:
• Comfortaa

Requirements
Must have
• Simple and Clean
Nice to have
• Easy to understand.

I the User am using Brava to connect with and communicate with Multiple Health Providers.
Should not have
• Only use our colors please along with White and Black

```html
<!DOCTYPE html>
<html lang="en">
<head>
<meta charset="utf-8">
<title>Brava Wellness – Connections</title>
<link rel="stylesheet" href="https://fonts.googleapis.com/css2?family=Rubik:wght@700;800&family=Comfortaa:wght@400;700&display=swap">
<style>
  :root {
    --blue: #1D44B8;
    --pink: #D85097;
    --black: #0A0A0A;
    --white: #FFFFFF;
    --paper: #F7F7FA;
    --backdrop: #EFEFF2;
    --ring-shade: #E6E6EA;
    --dash: #CFCFD4;
    --phone-edge: #D7D7DB;
  }
  html, body {
    margin: 0;
    padding: 0;
    width: 1037px;
    height: 1200px;
    overflow: hidden;
    background: var(--paper);
  }
  .poster { display: block; width: 1037px; height: 1200px; }
  .brand-name {
    font-family: "Rubik", "Arial Black", sans-serif;
    font-weight: 800;
    font-size: 200px;
    fill: var(--blue);
  }
  .label { font-family: "Rubik", "Arial Black", sans-serif; font-weight: 800; font-size: 44px; text-anchor: middle; }
  .label-blue { fill: var(--blue); }
  .label-pink { fill: var(--pink); }
  .spoke-blue { stroke: var(--blue); stroke-width: 5; }
  .spoke-pink { stroke: var(--pink); stroke-width: 5; }
  .app-text { font-family: "Comfortaa", sans-serif; }
  .app-name { font-size: 10px; fill: var(--white); font-weight: 700; }
  .app-meta { font-size: 7px; fill: var(--white); }
  .app-summary-head { font-size: 8px; fill: var(--pink); }
  .app-summary { font-size: 6.5px; fill: #333; }
  .app-nav { font-size: 8px; fill: var(--white); text-anchor: middle; }
  .app-status { font-size: 6px; fill: var(--white); }
</style>
</head>
<body>
<svg class="poster" viewBox="160 167 1480 1736" preserveAspectRatio="none" xmlns="http://www.w3.org/2000/svg">
  <defs>
    <linearGradient id="photo-tones" x1="0" y1="0" x2="0" y2="1">
      <stop offset="0" stop-color="#B79A8C"/>
      <stop offset="0.5" stop-color="#7A5C8E"/>
      <stop offset="1" stop-color="#5E55A8"/>
    </linearGradient>
  </defs>

  <rect class="page" x="160" y="167" width="1480" height="1736" fill="var(--paper)"/>

  <path class="backdrop" d="M222 957 H600 A420 420 0 0 1 1000 617 H1570 V1200 A430 430 0 0 1 1140 1630 H640 A420 420 0 0 1 222 1210 Z" fill="var(--backdrop)"/>

  <text class="brand-name" x="250" y="430" textLength="1300" lengthAdjust="spacingAndGlyphs">BRAVA WELLNESS</text>

  <circle cx="905" cy="1163" r="400" fill="none" stroke="var(--dash)" stroke-width="5" stroke-dasharray="28 12 4 12"/>

  <circle cx="905" cy="1163" r="292" fill="var(--ring-shade)"/>
  <circle cx="905" cy="1163" r="232" fill="var(--white)"/>

  <line class="spoke-blue" x1="890" y1="700" x2="890" y2="800"/>
  <line class="spoke-pink" x1="1250" y1="800" x2="1140" y2="905"/>
  <line class="spoke-blue" x1="1350" y1="1148" x2="1255" y2="1148"/>
  <line class="spoke-pink" x1="1235" y1="1455" x2="1160" y2="1385"/>
  <line class="spoke-blue" x1="920" y1="1600" x2="920" y2="1520"/>
  <line class="spoke-pink" x1="600" y1="1490" x2="660" y2="1430"/>
  <line class="spoke-blue" x1="460" y1="1180" x2="555" y2="1180"/>
  <line class="spoke-pink" x1="580" y1="870" x2="660" y2="945"/>

  <circle cx="905" cy="1163" r="337" fill="none" stroke="var(--pink)" stroke-width="58" pathLength="360" stroke-dasharray="42 48" transform="rotate(-88 905 1163)"/>
  <circle cx="905" cy="1163" r="337" fill="none" stroke="var(--blue)" stroke-width="58" pathLength="360" stroke-dasharray="42 48" transform="rotate(-43 905 1163)"/>

  <g class="node node-mind">
    <circle cx="890" cy="643" r="78" fill="var(--blue)"/>
    <circle cx="890" cy="643" r="60" fill="var(--white)"/>
    <circle cx="880" cy="632" r="14" fill="none" stroke="var(--blue)" stroke-width="7" stroke-dasharray="5 3"/>
    <circle cx="903" cy="650" r="9" fill="none" stroke="var(--blue)" stroke-width="6" stroke-dasharray="4 3"/>
  </g>
  <g class="node node-heart">
    <circle cx="400" cy="1185" r="78" fill="var(--blue)"/>
    <circle cx="400" cy="1185" r="60" fill="var(--white)"/>
    <path d="M400 1230 C360 1200 352 1185 352 1168 C352 1150 366 1140 380 1140 C390 1140 397 1146 400 1153 C403 1146 410 1140 420 1140 C434 1140 448 1150 448 1168 C448 1185 440 1200 400 1230 Z" fill="var(--blue)"/>
  </g>
  <g class="node node-body">
    <circle cx="1413" cy="1148" r="78" fill="var(--blue)"/>
    <circle cx="1413" cy="1148" r="60" fill="var(--white)"/>
    <circle cx="1413" cy="1148" r="44" fill="none" stroke="var(--blue)" stroke-width="3" stroke-dasharray="2 5"/>
    <path d="M1413 1140 C1404 1132 1398 1140 1413 1152 C1428 1140 1422 1132 1413 1140 Z" fill="var(--blue)"/>
  </g>
  <g class="node node-spirit">
    <circle cx="920" cy="1665" r="78" fill="var(--blue)"/>
    <circle cx="920" cy="1665" r="60" fill="var(--white)"/>
    <path d="M890 1700 L915 1678 L935 1690 L955 1700 Z" fill="var(--blue)"/>
    <path d="M902 1640 L932 1640 L928 1672 L906 1672 Z" fill="var(--blue)"/>
  </g>

  <g class="node node-family">
    <circle cx="533" cy="820" r="74" fill="var(--pink)"/>
    <rect x="493" y="805" width="18" height="46" rx="7" fill="var(--white)"/>
    <rect x="525" y="820" width="14" height="32" rx="6" fill="var(--white)"/>
    <rect x="554" y="805" width="18" height="46" rx="7" fill="var(--white)"/>
  </g>
  <g class="node node-friends">
    <circle cx="1250" cy="785" r="74" fill="var(--pink)"/>
    <rect x="1218" y="770" width="26" height="60" rx="9" fill="var(--white)"/>
    <rect x="1256" y="770" width="26" height="60" rx="9" fill="var(--white)"/>
  </g>
  <g class="node node-acquaintances">
    <circle cx="1280" cy="1507" r="74" fill="var(--pink)"/>
    <path d="M1250 1470 H1300 A16 16 0 0 1 1316 1486 V1508 A16 16 0 0 1 1300 1524 H1268 L1252 1538 V1524 A16 16 0 0 1 1234 1508 V1486 A16 16 0 0 1 1250 1470 Z" fill="var(--white)"/>
    <circle cx="1260" cy="1497" r="4" fill="var(--pink)"/>
    <circle cx="1275" cy="1497" r="4" fill="var(--pink)"/>
    <circle cx="1290" cy="1497" r="4" fill="var(--pink)"/>
  </g>
  <g class="node node-professionals">
    <circle cx="560" cy="1537" r="74" fill="var(--pink)"/>
    <rect x="512" y="1525" width="28" height="30" rx="10" fill="var(--white)"/>
    <rect x="544" y="1520" width="32" height="40" rx="11" fill="var(--white)"/>
    <rect x="580" y="1525" width="28" height="30" rx="10" fill="var(--white)"/>
  </g>

  <text class="label label-blue" x="892" y="540">MIND</text>
  <text class="label label-pink" x="525" y="705">FAMILY</text>
  <text class="label label-pink" x="1257" y="683">FRIENDS</text>
  <text class="label label-blue" x="397" y="1327">HEART</text>
  <text class="label label-blue" x="1418" y="1300">BODY</text>
  <text class="label label-pink" x="555" y="1677">PROFESSIONALS</text>
  <text class="label label-pink" x="1283" y="1670">ACQUAINTANCES</text>
  <text class="label label-blue" x="920" y="1820">SPIRIT</text>

  <g class="app">
    <rect x="783" y="907" width="242" height="505" rx="40" fill="var(--white)" stroke="var(--phone-edge)" stroke-width="3"/>
    <circle cx="904" cy="922" r="3" fill="#444"/>
    <rect x="886" y="934" width="38" height="4" rx="2" fill="#444"/>
    <circle cx="866" cy="937" r="3" fill="#444"/>
    <circle cx="904" cy="1380" r="17" fill="none" stroke="#555" stroke-width="2"/>

    <rect x="796" y="965" width="218" height="387" fill="var(--white)"/>
    <rect x="796" y="965" width="218" height="297" rx="6" fill="url(#photo-tones)" role="img" aria-label="Photo of the resident with two family members"/>
    <text class="app-text app-status" x="802" y="976">●●● BELL</text>
    <text class="app-text app-status" x="893" y="976">4:21 PM</text>
    <text class="app-text app-status" x="977" y="976">100%</text>
    <text class="app-text app-name" x="807" y="1236">Walter Brenning, 97</text>
    <text class="app-text app-meta" x="807" y="1246">Resident</text>
    <text class="app-text app-meta" x="807" y="1255">Maple Grove Care Home</text>
    <rect x="981" y="1229" width="18" height="13" rx="2" fill="none" stroke="var(--white)" stroke-width="1.5"/>

    <text class="app-text app-summary-head" x="809" y="1277">Summary</text>
    <text class="app-text app-summary" x="809" y="1288">I'm Walter, blessed husband to my beautiful bride</text>
    <text class="app-text app-summary" x="809" y="1296">Ilse, Dad to my 2 amazing daughters…</text>

    <rect x="796" y="1307" width="218" height="45" fill="var(--blue)"/>
    <path d="M815 1326 L822 1319 L829 1326 V1333 H815 Z" fill="none" stroke="var(--white)" stroke-width="1.5"/>
    <circle cx="874" cy="1323" r="5" fill="none" stroke="var(--white)" stroke-width="1.5"/>
    <line x1="878" y1="1327" x2="882" y2="1331" stroke="var(--white)" stroke-width="1.5"/>
    <rect x="921" y="1318" width="20" height="13" fill="none" stroke="var(--white)" stroke-width="1.5"/>
    <path d="M921 1318 L931 1326 L941 1318" fill="none" stroke="var(--pink)" stroke-width="1.5"/>
    <path d="M986 1332 C978 1326 976 1322 976 1320 C976 1316 982 1314 986 1319 C990 1314 996 1316 996 1320 C996 1322 994 1326 986 1332 Z" fill="none" stroke="var(--white)" stroke-width="1.5"/>
    <text class="app-text app-nav" x="822" y="1343">Home</text>
    <text class="app-text app-nav" x="876" y="1343">Search</text>
    <text class="app-text app-nav" x="931" y="1343">Inbox</text>
    <text class="app-text app-nav" x="986" y="1343">Post</text>
  </g>
</svg>
</body>
</html>
```